Business Card for a Jewellery Brand

Business card for an upscale jewellery brand. Attached is the brand logo and icon and color board. I am looking for two card versions: one for the founder and one is generic. The card should be elegant and convey upscale and premium feel. I am open to both square and rectangle card shapes.

Industry/Entity Type

Jewelry

Contact Information for Business Card

Two cards: (1) Sunila Perumbadi (Founder) (2) General
(1) Sunila Perumbadi card should have Name: Sunila Perumbadi, Title: Founder Email id: sunila@quelm.com.au. Phone no: +61412555307
(2) Generic card should have Email id: info@quelm.com.au. Phone no: +61431555962

Requirements
Must have
• Workmark
• ICON
• Phone no
• Email ID
• ABN: 48917205563 (Note: ABN is Business number in Australia)
• Website: www.quelm.com.au
• Instagram: quelm_jewellery
• Facebook: @quelmjewellery
Nice to have
• Tagline

```html
<!DOCTYPE html>
<html lang="en">
<head>
<meta charset="utf-8">
<title>Quelm – Business Cards</title>
<link rel="stylesheet" href="https://fonts.googleapis.com/css2?family=Questrial&display=swap">
<style>
  :root {
    --backdrop: #0c0c0c;
    --card-white: #fbfbfc;
    --marble-grey: #e9ecef;
    --coral: #e8928d;
    --coral-deep: #dc8580;
    --blush: #ec9d97;
    --ink: #4a4a4a;
    --paper-text: #ffffff;
  }
  * { box-sizing: border-box; margin: 0; padding: 0; }
  html, body {
    width: 1200px; height: 1000px; overflow: hidden;
    background: var(--backdrop);
    font-family: "Questrial", "Century Gothic", sans-serif;
  }
  .card-set {
    position: absolute; top: 347px; left: 50px;
    display: flex; gap: 60px;
  }
  .card {
    position: relative; width: 520px; height: 306px;
    border-radius: 14px; overflow: hidden;
  }
  .marble-texture { position: absolute; inset: 0; }

  /* Founder card */
  .card--founder { background: var(--card-white); color: var(--ink); }
  .card--founder .marble-texture {
    background:
      radial-gradient(ellipse at 25% 30%, var(--marble-grey) 0%, transparent 45%),
      radial-gradient(ellipse at 80% 75%, var(--marble-grey) 0%, transparent 40%);
    opacity: .8;
  }
  .founder-brand {
    position: absolute; top: 62px; left: 0; right: 0;
    text-align: center; color: var(--coral);
    font-size: 26px; letter-spacing: 8px;
  }
  .founder-name {
    position: absolute; top: 122px; left: 0; right: 0;
    text-align: center; font-size: 19px; line-height: 1.15;
  }
  .founder-name .role { display: block; font-size: 17px; }
  .divider {
    position: absolute; left: 30px; right: 30px; top: 183px;
    height: 2px; background: var(--coral);
  }
  .contact-row {
    position: absolute; left: 30px; right: 30px; top: 215px;
    display: flex; justify-content: space-between;
    font-size: 14px;
  }

  /* Brand card */
  .card--brand { background: var(--blush); color: var(--paper-text); }
  .card--brand .marble-texture {
    background:
      radial-gradient(ellipse at 30% 40%, var(--coral-deep) 0%, transparent 50%),
      radial-gradient(ellipse at 75% 70%, var(--coral-deep) 0%, transparent 45%);
    opacity: .7;
  }
  .brand-wordmark {
    position: absolute; top: 88px; left: 0; right: 0;
    text-align: center; font-size: 68px; letter-spacing: 26px;
    padding-left: 26px;
  }
  .brand-footer {
    position: absolute; left: 28px; right: 28px; bottom: 36px;
    display: flex; justify-content: space-between; align-items: center;
    font-size: 14px;
  }
  .social { display: flex; align-items: center; gap: 8px; font-size: 15px; }
  .social-dot {
    width: 14px; height: 14px; border-radius: 50%;
    background: var(--paper-text);
  }
</style>
</head>
<body>
  <main class="card-set">
    <section class="card card--founder" aria-label="Founder card">
      <div class="marble-texture" role="img" aria-label="Faint grey marble texture"></div>
      <div class="founder-brand">QUELM</div>
      <p class="founder-name">Sunila Perumbadi<span class="role">Founder</span></p>
      <div class="divider"></div>
      <div class="contact-row">
        <span class="contact-phone">+61 41 25 55 307</span>
        <span class="contact-web">www.quelm.com.au</span>
        <span class="contact-email">sunila@quelm.com.au</span>
      </div>
    </section>

    <section class="card card--brand" aria-label="Brand card">
      <div class="marble-texture" role="img" aria-label="Soft coral marble texture"></div>
      <div class="brand-wordmark">QUELM</div>
      <div class="brand-footer">
        <span class="abn">ABN: 48917205563</span>
        <span class="social social--instagram"><span class="social-dot"></span>quelm_jewellery</span>
        <span class="social social--facebook"><span class="social-dot"></span>@quelmjewellery</span>
      </div>
    </section>
  </main>
</body>
</html>
```